New counselling and hypnotherapy business

I'd like a flyer which is relevant to people who want support and to improve their wellbeing which follows the same theme as my website: http://larkmoretherapy.plumweave.com
And emphasise that whatever the area of concern, development or growth and I can tailor my knowledge and skills to help.

I'd like to use the same logo and my emphasis is to draw the audience in...therapy and counselling is for people who are "stuck" and having a difficult time...it can also be useful has a personal development tool.

Hypnotherapy

```html
<!DOCTYPE html>
<html lang="en">
<head>
<meta charset="utf-8">
<title>Larkmore Counselling &amp; Hypnotherapy Flyer</title>
<link rel="stylesheet" href="https://fonts.googleapis.com/css2?family=Lato:wght@400;700&family=Rokkitt:wght@500;600;700&display=swap">
<style>
  :root {
    --purple: #7a3f7a;
    --purple-dark: #5a2a5c;
    --purple-light: #9a5d98;
    --text: #2f2f2f;
    --panel-border: #cfcfcf;
    --page: #ffffff;
    --backdrop: #ffffff;
  }
  * { box-sizing: border-box; margin: 0; padding: 0; }
  html, body { width: 959px; height: 1200px; overflow: hidden; background: var(--backdrop); }
  body { position: relative; font-family: 'Lato', sans-serif; color: var(--text); }

  .flyer {
    position: absolute; left: 55px; top: 50px; width: 850px; height: 1100px;
    background: var(--page); box-shadow: 0 2px 8px rgba(0,0,0,0.35);
  }
  .hero {
    position: absolute; left: 0; top: 0; width: 850px; height: 220px;
    background: linear-gradient(180deg, #3a3a3a 0%, #8d8d8a 38%, #c9c7c0 52%, #5a5a58 62%, #2a2a2a 100%);
  }
  .hero-title {
    position: absolute; left: 26px; top: 60px;
    font-family: 'Rokkitt', serif; font-weight: 700; font-size: 37px; line-height: 44px;
    color: #fff; letter-spacing: 0.5px;
  }
  .hero-band {
    position: absolute; left: 0; top: 220px; width: 850px; height: 40px;
    background: linear-gradient(90deg, var(--purple-dark), var(--purple) 50%, var(--purple-dark));
  }

  .info-panel {
    position: absolute; left: 15px; top: 272px; width: 820px; height: 450px;
    border: 2px solid var(--panel-border); border-radius: 3px;
    background: linear-gradient(90deg, #ffffff 0%, #ececec 40%, #ffffff 41%, #f3f3f3 100%);
    box-shadow: 0 4px 6px rgba(0,0,0,0.12);
  }
  .pill {
    position: absolute; height: 23px; padding: 0 10px;
    background: var(--purple); color: #fff; border-radius: 12px;
    font-family: 'Rokkitt', serif; font-weight: 600; font-size: 16px; line-height: 23px; letter-spacing: 0.3px;
    box-shadow: 1px 1px 2px rgba(0,0,0,0.3);
  }
  .copy {
    position: absolute; font-size: 15px; line-height: 18.4px; text-align: justify;
    font-weight: 400; color: var(--text); hyphens: auto; -webkit-hyphens: auto;
  }
  .copy p + p { margin-top: 18.4px; }
  .price {
    position: absolute; left: 344px; top: 285px;
    font-family: 'Rokkitt', serif; font-weight: 600; font-size: 17px; color: var(--purple); letter-spacing: 0.3px;
  }

  .services {
    position: absolute; left: 23px; top: 750px; width: 215px; height: 258px;
  }
  .services-cap {
    position: absolute; left: 0; top: 0; width: 215px; height: 12px;
    background: var(--purple); border-radius: 14px 14px 0 0;
  }
  .services-title {
    position: absolute; left: 19px; top: 14px; z-index: 1;
    font-family: 'Rokkitt', serif; font-weight: 600; font-size: 17px; line-height: 20px;
    color: var(--purple); letter-spacing: 0.5px;
  }
  .services-body {
    position: absolute; left: 0; top: 35px; width: 215px; height: 223px;
    background: linear-gradient(180deg, var(--purple-light), var(--purple) 40%, var(--purple-dark));
    border-radius: 0 0 22px 22px;
  }
  .services-list {
    position: absolute; left: 27px; top: 5px; list-style: none;
    color: #fff; font-weight: 700; font-size: 14.6px; line-height: 16.6px;
  }

  .portrait-ring {
    position: absolute; left: 262px; top: 770px; width: 206px; height: 206px;
    border-radius: 50%; background: var(--purple); padding: 12px;
  }
  .portrait {
    width: 100%; height: 100%; border-radius: 50%;
    background: radial-gradient(circle at 50% 40%, #d9a88a 0%, #b98a6e 30%, #c45a6a 70%, #9b3f55 100%);
    border: 3px solid #fff;
  }

  .brand {
    position: absolute; left: 543px; top: 765px; width: 270px; height: 190px;
  }
  .brand-mark {
    position: absolute; left: 100px; top: 10px; width: 70px; height: 70px; border-radius: 50%; background: var(--purple);
  }
  .brand-name {
    position: absolute; left: 0; top: 112px; width: 270px; text-align: center;
    font-family: 'Rokkitt', serif; font-weight: 500; font-size: 25px; line-height: 24px; color: var(--purple);
  }
  .website {
    position: absolute; left: 493px; top: 983px;
    font-family: 'Rokkitt', serif; font-weight: 600; font-size: 17px; color: var(--purple); letter-spacing: 0.8px;
  }

  .footer {
    position: absolute; left: 0; top: 1015px; width: 850px; height: 85px;
    background: linear-gradient(90deg, var(--purple-dark), var(--purple) 50%, var(--purple-dark));
    color: #fff;
  }
  .address-label {
    position: absolute; left: 45px; top: 7px;
    font-family: 'Rokkitt', serif; font-weight: 600; font-size: 16px; letter-spacing: 0.5px;
  }
  .address {
    position: absolute; left: 28px; top: 27px; font-style: normal; font-size: 10.5px; line-height: 11px;
  }
  .contact {
    position: absolute; left: 618px; top: 16px; font-size: 10.5px; line-height: 22px;
  }
  .contact b { font-family: 'Rokkitt', serif; font-weight: 600; font-size: 15px; }
</style>
</head>
<body>
<main class="flyer">
  <header class="hero" role="img" aria-label="Photo of a family walking hand in hand along a beach at sunset">
    <h1 class="hero-title">RELAX<br>FREE YOUR MIND<br>TAKE CONTROL</h1>
  </header>
  <div class="hero-band"></div>

  <section class="info-panel">
    <h2 class="pill" style="left:18px; top:8px;">WHAT IS HYPNOTHERAPY?</h2>
    <div class="copy" style="left:21px; top:38px; width:300px;">
      <p>What comes to mind? You may conjure up images or thoughts of stage shows. In reality, real hypnosis bears little resemblance to that and can be far more beneficial.</p>
      <p>It's all about slowing down the pace of life in order to allow your mind to receive positive suggestions for change. You've probably already experienced something similar to hypnosis and not even known it.</p>
      <p>Have you ever been on a train journey, sat there with half-closed eyes, day-dreaming or driven a journey and suddenly wonder how you reached your destination? In that boundary between sleep and awake our brain produces alpha waves - that's where</p>
      <p>I can help guide your unconscious mind to solve the problems that your conscious brain can't do on its own.</p>
    </div>

    <h2 class="pill" style="left:338px; top:8px;">WHAT DO I DO AS THE HYPNOTHERAPIST?</h2>
    <div class="copy" style="left:344px; top:38px; width:458px;">
      <p>Hypnotherapy is a very relaxing process and it is my role to provide a safe and trusted environment where you can allow yourself to relax and slow down your mind. I do this through recognised relaxation techniques which then allow you to focus on the story I take you through, with the appropriate personalisation and suggestions included.</p>
    </div>

    <h2 class="pill" style="left:338px; top:158px;">WHAT'S IT USEFUL FOR?</h2>
    <div class="copy" style="left:344px; top:188px; width:458px;">
      <p>I can carry out short term (1-3 sessions) tailored hypnotherapy which is useful for a wide range of areas as listed in the box on the right of this screen. I am also able, in longer term work, to provide Hypnotherapy in conjunction with counselling or other techniques as is appropriate for you.</p>
    </div>
    <p class="price">COST: £40 PER ONE HOUR SESSION</p>

    <h2 class="pill" style="left:338px; top:318px;">WHAT IS COUNSELLING?</h2>
    <div class="copy" style="left:344px; top:348px; width:458px;">
      <p>It's about being able to have a safe and trusted environment where you feel comfortable to share whatever is going on for you, problems, concerns, areas you'd like to personally develop. Essentially, it's time for you to just be you, free from any form of judgement.</p>
    </div>
  </section>

  <aside class="services">
    <div class="services-cap"></div>
    <h3 class="services-title">COUNSELLING</h3>
    <div class="services-body">
      <ul class="services-list">
        <li>Grief and Loss</li>
        <li>Anxiety</li>
        <li>Depression</li>
        <li>Stress</li>
        <li>Relationships</li>
        <li>Self esteem</li>
        <li>Confidence</li>
        <li>Personal development</li>
        <li>Self harm</li>
        <li>Sexual concerns</li>
        <li>Eating disorders</li>
        <li>Abuse</li>
      </ul>
    </div>
  </aside>

  <div class="portrait-ring">
    <div class="portrait" role="img" aria-label="Portrait photo of the therapist"></div>
  </div>

  <div class="brand">
    <span class="brand-mark"></span>
    <p class="brand-name">Larkmore<br>Counselling &amp;<br>Hypnotherapy</p>
  </div>
  <p class="website">LARKMORETHERAPY.PLUMWEAVE.COM</p>

  <footer class="footer">
    <h4 class="address-label">ADDRESS.</h4>
    <address class="address">Larkmore Counselling &amp; Hypnotherapy,<br>12B, Mill Lane,<br>Brackhurst<br>West Fenwold BR4 6LT</address>
    <div class="contact">
      <div><b>Tel.</b> 07700 900418</div>
      <div><b>Email.</b>larkmoretherapy@mailbox.net</div>
    </div>
  </footer>
</main>
</body>
</html>
```